Book Cover Design Project - SIMPLE ART, Pre-Concepted

We already have a full design concept for the cover art. It is however in a low quality word document format. This project is to recreate existing example guideline art in as much vector art possible for great quality print production. Artistic flare is welcome. This will be for a book cover (front/back) and I want the quality to be excellent.

Art to be provided in Adobe Illustrator format. The book will be 6wide x 9high, so the artboard for the cover needs to be set up to 12.5 wide x 9 high with .125" bleeds.

Copy content for the spine: "Beneath a Copper Evening Sky Still" RL Moskowicz.

Here is a link to download the word document "template" and a new photo for the back page. I'm not sure that I like the new photo, it is possible the old one in the word document will work.

www.bluemarlinpressworks.com/uploads/QuillHavenSharedFiles.zip

I've got a fast deadline on this project because the client would like to have manufacturing completed by Christmas...which is why this is only a 2 day project. I appreciate your interest in our project.

Gordon

Try this link...seems I was missing the .zip extension which may have been causing problems.

Requirements
Must have
• Adobe Illustrator Files
CMYK color setup - no color definitions for project
Artboard Size: 12.625 wide x 9.125 high
Art Orientation: Flat image should have the back book page on the left side, front page on the right side, spine copy running down the middle.

```html
<!DOCTYPE html>
<html lang="en">
<head>
<meta charset="utf-8">
<title>Beneath a Copper Evening Sky Still — Cover Spread</title>
<link href="https://fonts.googleapis.com/css2?family=Anton&family=Jost:wght@400;700&family=Pathway+Gothic+One&display=swap" rel="stylesheet">
<style>
  :root {
    --cover-red: #c01f2f;
    --paper: #ffffff;
    --ink: #111111;
    --frame-grey: #c9c9c9;
    --subtitle-pink: #f3dcdc;
    --guide: #333333;
  }
  html, body { margin: 0; padding: 0; overflow: hidden; background: var(--paper); }
  .spread {
    position: relative; width: 1200px; height: 870px; overflow: hidden;
    background: var(--paper);
  }
  .band {
    position: absolute; left: 0; top: 289px; width: 1200px; height: 61px;
    background: var(--cover-red);
  }
  .back-panel {
    position: absolute; left: 59px; top: 0; width: 461px; height: 743px;
    background: var(--cover-red);
  }
  .front-panel {
    position: absolute; left: 733px; top: 0; width: 337px; height: 743px;
    background: var(--cover-red);
  }
  .spine-guide {
    position: absolute; top: 0; height: 870px; width: 0;
    border-left: 1px dashed var(--guide);
  }
  .trim-guide { position: absolute; background: var(--guide); }

  .about {
    position: absolute; left: 22px; top: 50px; width: 418px;
    font-family: "Jost", sans-serif; font-size: 12.4px; line-height: 15.6px;
    color: var(--paper); text-align: justify;
  }
  .about p { margin: 0 0 15px; }
  .author-photo {
    float: left; width: 171px; height: 196px; margin: 0 14px 6px 0;
    border: 3px solid var(--frame-grey);
    background: linear-gradient(160deg, #d9cbb8 0%, #a08a72 45%, #2d2a30 100%);
  }
  .about .lead { font-weight: 700; font-size: 13px; line-height: 15.4px; text-align: left; }

  .spine-author, .spine-title {
    position: absolute; font-family: "Pathway Gothic One", sans-serif;
    writing-mode: vertical-rl; white-space: nowrap; line-height: 1;
  }
  .spine-author { left: 583px; top: 142px; font-size: 35px; color: var(--ink); }
  .spine-title { left: 583px; top: 372px; font-size: 31px; color: var(--cover-red); }

  .title-word {
    position: absolute; margin: 0; font-family: "Anton", sans-serif; font-weight: 400;
    color: var(--paper); white-space: nowrap; line-height: 1;
  }
  .title-top { left: 733px; width: 337px; top: 108px; font-size: 48px; text-align: center; }
  .title-left { left: 628px; width: 105px; top: 296px; font-size: 40px; text-align: right; }
  .title-right { left: 1076px; top: 296px; font-size: 40px; }
  .title-bottom { left: 733px; width: 337px; top: 554px; font-size: 48px; text-align: center; }

  .cover-image {
    position: absolute; left: 760px; top: 174px; width: 279px; height: 362px;
    border: 3px solid var(--frame-grey);
    background: radial-gradient(ellipse at 55% 35%, #f4ede4 0%, #b9aa98 30%, #4c433c 65%, #1d1a18 100%);
  }
  .subtitle {
    position: absolute; left: 733px; width: 337px; top: 674px; margin: 0;
    font-family: "Pathway Gothic One", sans-serif; font-size: 27px; line-height: 34px;
    color: var(--subtitle-pink); text-align: center;
  }
</style>
</head>
<body>
<div class="spread">
  <div class="band"></div>

  <section class="back-panel">
    <div class="about">
      <div class="author-photo" role="img" aria-label="Portrait photograph of the author"></div>
      <p class="lead">About the author: The word of God says that “I know the plans I have for you” (Jeremiah 29:11) and that “before I formed you in the womb I knew you” (Jeremiah 1:15). These verses of scripture depict the life of Reuben L Moskowicz.</p>
      <p>As a little boy Reuben was always told that he was going to be a preacher. The magnitude of this repeated statement and exactly what it entailed was not taken seriously or truly understood, at that time. It was not Reuben’s plan or desire to be a preacher, and he tried to do anything and everything to avoid the talks of him becoming one. Reuben’s path of life, although he believed in God, took him down the road that led him away from God. His struggles with life’s events and being an introvert kept him emotionally troubled, in a state of depression and wanting to commit suicide. Yet, as the Lord was with Jeremiah, even so was the Lord with Reuben. The Lord was to show Reuben just what it meant to have complete trust in Him and to know that He would always provide a way of an escape. Before Reuben came to the point of carrying out his plans to commit suicide, he prayed a simple prayer that God would give him a new family. At that exact moment Reuben’s life began to take a new direction. He began to seek after the Lord; it became his quest to find out what it meant to be a servant of God. Because of his being an introvert, he began to write his emotions on paper in the form of poems. Those poems gave him the strength to come out of depression and began his two year journey to find God.</p>
      <p>Reuben’s relationship with Jesus and salvation journey began at the age of nineteen. The poetry writing started as a therapeutic remedy for his troubled past, but developed into the psalms of Reuben because of God’s grace and mercy that delivered him from despair and hopelessness.</p>
      <p>God’s favor covers Reuben’s life and carries him from day to day. It is written that “without me (Christ) ye can do nothing” (John 15:5). This scripture resonates in Reuben’s heart. For, he truly believes that God is the author and he is just the vessel used of God. His desire is that each poem will be taken personally and become a tool used by everyone to help them on their Christian journey and to let them know that they are never alone in their experience and quest to be closer to the Lord Jesus Christ.</p>
    </div>
  </section>

  <div class="spine-guide" style="left:576px"></div>
  <div class="spine-guide" style="left:623px"></div>
  <div class="spine-author">RL Moskowicz</div>
  <div class="spine-title">Beneath a Copper Evening Sky Still</div>

  <section class="front-panel"></section>
  <h1 class="title-word title-top">Beneath a</h1>
  <span class="title-word title-left">Copper</span>
  <span class="title-word title-right">Evening</span>
  <div class="cover-image" role="img" aria-label="Photograph of a dark cross silhouetted against a glowing light"></div>
  <span class="title-word title-bottom">Sky Still</span>
  <p class="subtitle">A compilation of poems<br>by RL Moskowicz</p>

  <div class="trim-guide" style="left:59px; top:743px; width:1px; height:127px"></div>
  <div class="trim-guide" style="left:1070px; top:743px; width:1px; height:127px"></div>
  <div class="trim-guide" style="left:0; top:857px; width:1200px; height:1px"></div>
</div>
</body>
</html>
```